Inspiring Poster for Company Staff Room

What we need:
We want an awesome design to create a poster that will be plaque mounted in our staff room. We just went through a very motivating workshop to discover our "WHY" as a company...basically, to define the reason we are in business, and to define what motivates us to come to work every day. The poster must be motivating but really resonate with our team…we are not looking for a “typical” motivational poster that we can purchase off Amazon!

Who we are:
We are a property management company, a team of 20 that is passionate about our investors, and residents who rent from us, but more importantly, we love helping people and making a difference in our industry. We are proud and work hard for every single 5 star Google review we achieve.

Information for you:
We have included a mock up of the poster, which words we want, and the placement of them (in a general sense) but we need a designer to really bring this together in an inspiring poster that represents our company’s culture, feel, and fit. We have also included a logo file, as well as examples of our business cards, letterhead and thank you card already designed.
Here are the parameters:

(1) Poster size: 24” x 36”
(2) Full colour
(3) Must incorporate our company logo
(4) Must incorporate the following words:

Why do I come to work?

“To feel fulfilled by empathizing, educating and empowering our clients and co-workers so that we can build strong, impactful relationships”

Own the outcome

(5) Please see our website at www.brindlecovepm.com to get a feel for our company culture and for a better idea of our current company graphics

Target Market(s)

Our staff. Will not be seen by our clients

Industry/Entity Type

Real Estate

Font styles to use
Serif
Sans Serif

Requirements
Should not have
• Would not want this to be too "busy." if you can picture it, the poster will be mounted on the wall as soon as someone enters the room. The idea is to remind them each day why they come to work.

```html
<!DOCTYPE html>
<html lang="en">
<head>
<meta charset="utf-8">
<title>Why do I come to work? – Poster Concepts</title>
<link rel="stylesheet" href="https://fonts.googleapis.com/css2?family=Playfair+Display:wght@700;900&family=Montserrat:ital,wght@0,300;0,600;0,800;0,900;1,600;1,900&family=Raleway:wght@300;800&display=swap">
<style>
  :root {
    --blue: #0792cf;
    --ink: #3b3b3b;
    --paper: #ffffff;
    --mist: #eeeff1;
    --line: #0792cf;
  }
  * { margin: 0; padding: 0; box-sizing: border-box; }
  html, body { width: 1082px; height: 1200px; overflow: hidden; background: var(--paper); }
  body { position: relative; font-family: "Raleway", sans-serif; color: var(--ink); }

  .poster { position: absolute; overflow: hidden; background: var(--paper); box-shadow: 0 1px 4px rgba(0,0,0,.3); }
  .poster--a { left: 175px; top: 82px; width: 356px; height: 533px; }
  .poster--b { left: 562px; top: 82px; width: 356px; height: 533px; background: var(--blue); }
  .poster--c { left: 34px; top: 666px; width: 328px; height: 492px; }
  .poster--d { left: 383px; top: 666px; width: 328px; height: 492px; }
  .poster--e { left: 731px; top: 670px; width: 328px; height: 491px; }

  .brand { position: absolute; display: flex; align-items: center; gap: 5px; font-family: "Montserrat", sans-serif; font-weight: 800; color: var(--blue); line-height: 1; }
  .brand__mark { width: 13px; height: 13px; background: var(--ink); }
  .brand__name { font-size: 11px; letter-spacing: .5px; text-transform: uppercase; }
  .brand__name small { display: block; font-size: 5px; font-weight: 800; letter-spacing: 1px; margin-top: 2px; }
  .poster--b .brand { color: var(--paper); }
  .poster--b .brand__mark { background: var(--paper); }

  .why { position: absolute; font-family: "Playfair Display", serif; font-weight: 900; color: var(--ink); line-height: 1; }
  .why__big { display: block; font-size: 70px; letter-spacing: -3px; }
  .why__sub { position: relative; display: block; font-size: 22px; font-weight: 700; color: var(--blue); margin-top: -8px; }
  .why__sub span { margin-left: 34px; }
  .poster--b .why__sub { color: var(--paper); }

  .mission { position: absolute; font-family: "Raleway", sans-serif; font-weight: 300; color: var(--ink); }
  .mission b { font-family: "Montserrat", sans-serif; font-weight: 800; }
  .mission--framed { left: 30px; top: 210px; font-size: 20.5px; line-height: 29px; letter-spacing: -.5px; }
  .mission--framed .lg { font-size: 26px; letter-spacing: -1px; }

  .frame { position: absolute; inset: 0; width: 100%; height: 100%; }
  .frame path { fill: none; stroke: var(--line); stroke-width: 1; }
  .poster--b .frame path { stroke: #cfe9f6; }

  .outcome { position: absolute; font-family: "Playfair Display", serif; font-weight: 900; color: var(--blue); font-size: 22px; line-height: 1; white-space: nowrap; }
  .poster--b .outcome { color: var(--paper); }

  .why-sans { position: absolute; left: 30px; top: 76px; font-family: "Montserrat", sans-serif; font-weight: 900; line-height: 1; }
  .why-sans__big { display: block; font-size: 46px; color: var(--blue); -webkit-text-stroke: 1px #04658f; letter-spacing: -1px; }
  .why-sans__sub { display: block; font-size: 22px; color: var(--ink); margin-top: 4px; }
  .why-sans__sub span { color: var(--blue); }
  .mission--italic { left: 27px; top: 172px; font-family: "Montserrat", sans-serif; font-style: italic; font-weight: 600; font-size: 18px; line-height: 28.5px; }
  .mission--italic .accent { color: var(--blue); font-weight: 900; font-size: 22px; }
  .mission--italic .heavy { font-weight: 900; font-size: 26px; }
  .outcome-stack { position: absolute; right: 26px; top: 380px; font-family: "Montserrat", sans-serif; font-weight: 900; text-align: right; line-height: .9; }
  .outcome-stack__own { display: block; font-size: 54px; color: var(--blue); -webkit-text-stroke: 1px #04658f; }
  .outcome-stack__rest { display: block; font-size: 21px; color: var(--ink); }

  .skyline { position: absolute; }
  .skyline--line { left: 0; right: 0; bottom: 0; height: 110px; background: linear-gradient(to top, #d5ecf8, rgba(213,236,248,0)); }
  .skyline--faint { left: 0; right: 0; bottom: 0; height: 340px; background: linear-gradient(to top, #eceef0 0%, #f5f6f7 60%, rgba(255,255,255,0) 100%); }

  .mission--plain { left: 29px; top: 160px; font-size: 19px; line-height: 30.5px; letter-spacing: -.4px; }
  .mission--plain .lg { font-size: 25px; letter-spacing: -.8px; }

  .shapes { position: absolute; inset: 0; width: 100%; height: 100%; }
  .fill-blue { fill: var(--blue); }
  .fill-ink { fill: var(--ink); }
</style>
</head>
<body>

<section class="poster poster--a">
  <div class="brand" style="left:192px;top:22px"><span class="brand__mark"></span><span class="brand__name">Brindle Cove<small>Property Management</small></span></div>
  <h1 class="why" style="left:30px;top:86px"><span class="why__big">Why</span><span class="why__sub">do I come <span>to work?</span></span></h1>
  <svg class="frame" viewBox="0 0 356 533" aria-hidden="true"><path d="M248 232 H328 V449 H322"/><path d="M36 413 V449 H118"/></svg>
  <p class="mission mission--framed">To feel <b class="lg">fulfilled by</b><br>empathizing,<br>educating<br>and empowering our<br><b class="lg">clients and co-workers</b><br>so that we can <b class="lg">build</b><br>strong, impactful relationships</p>
  <p class="outcome" style="left:125px;top:438px">Own the Outcome</p>
</section>

<section class="poster poster--b">
  <div class="brand" style="left:188px;top:22px"><span class="brand__mark"></span><span class="brand__name">Brindle Cove<small>Property Management</small></span></div>
  <h1 class="why" style="left:30px;top:86px"><span class="why__big">Why</span><span class="why__sub">do I come <span>to work?</span></span></h1>
  <svg class="frame" viewBox="0 0 356 533" aria-hidden="true"><path d="M248 232 H328 V449 H322"/><path d="M36 413 V449 H118"/></svg>
  <p class="mission mission--framed">To feel <b class="lg">fulfilled by</b><br>empathizing,<br>educating<br>and empowering our<br><b class="lg">clients and co-workers</b><br>so that we can <b class="lg">build</b><br>strong, impactful relationships</p>
  <p class="outcome" style="left:125px;top:438px">Own the Outcome</p>
</section>

<section class="poster poster--c">
  <div class="brand" style="left:100px;top:26px"><span class="brand__mark"></span><span class="brand__name">Brindle Cove<small>Property Management</small></span></div>
  <h1 class="why-sans"><span class="why-sans__big">Why</span><span class="why-sans__sub">do I come <span>to work?</span></span></h1>
  <p class="mission mission--italic">To <span class="accent">feel fulfilled</span> by<br>empathizing, educating<br>and empowering our<br>clients and co-workers<br>so that <span class="heavy">we can build</span><br>strong, impactful<br>relationships.</p>
  <div class="skyline skyline--line" role="img" aria-label="Line drawing of a city skyline with a tall observation tower"></div>
  <p class="outcome-stack"><span class="outcome-stack__own">Own</span><span class="outcome-stack__rest">the Outcome</span></p>
</section>

<section class="poster poster--d">
  <div class="skyline skyline--faint" role="img" aria-label="Faint grey city skyline with a tall observation tower"></div>
  <svg class="shapes" viewBox="0 0 328 492" aria-hidden="true">
    <rect class="fill-blue" x="0" y="0" width="328" height="7"/>
    <polygon class="fill-blue" points="0,0 170,0 95,42"/>
    <polygon class="fill-ink" points="120,492 218,443 328,492"/>
    <rect class="fill-ink" x="0" y="487" width="328" height="5"/>
  </svg>
  <div class="brand" style="left:176px;top:26px"><span class="brand__mark"></span><span class="brand__name">Brindle Cove<small>Property Management</small></span></div>
  <h1 class="why" style="left:29px;top:62px"><span class="why__big">Why</span><span class="why__sub">do I come <span>to work?</span></span></h1>
  <p class="mission mission--plain">To <b class="lg">feel fulfilled</b> by<br>empathizing,<br>educating<br>and empowering our<br>clients and co-workers<br>so that we can build strong,<br>impactful <b class="lg">relationships</b></p>
  <p class="outcome" style="left:28px;top:406px">Own the Outcome</p>
</section>

<section class="poster poster--e">
  <div class="skyline skyline--faint" role="img" aria-label="Faint grey city skyline with a tall observation tower"></div>
  <svg class="shapes" viewBox="0 0 328 491" aria-hidden="true">
    <polygon class="fill-ink" points="0,0 95,0 95,42"/>
    <polygon class="fill-blue" points="95,0 188,0 95,42"/>
    <polygon class="fill-ink" points="118,491 205,452 205,491"/>
    <polygon class="fill-blue" points="205,452 290,491 205,491"/>
  </svg>
  <div class="brand" style="left:176px;top:22px"><span class="brand__mark"></span><span class="brand__name">Brindle Cove<small>Property Management</small></span></div>
  <h1 class="why" style="left:29px;top:62px"><span class="why__big">Why</span><span class="why__sub">do I come <span>to work?</span></span></h1>
  <p class="mission mission--plain" style="top:156px">To feel fulfilled by<br><b class="lg">empathizing,<br>educating<br>and empowering</b> our<br>clients and co-workers<br>so that we can build strong,<br>impactful <b class="lg">relationships</b></p>
  <p class="outcome" style="left:100px;top:402px">Own the Outcome</p>
</section>

</body>
</html>
```